Need a business card design for a residential architect.

You can get a sense of his work at www.tbrolvik.com

Would like a consistent look and feel between business card and website
.

Target Market(s)

Residential homeowners builders

Industry/Entity Type

Residential

Contact Information for Business Card

Dale Brolvik
Principle
Brolvik Architecture
418 Quill Lane
Menlo Park, CA 94025

dale@tbrolvik.com

tbrolvik.com
phone: 650-555-0172
Fax: 650-555-0196

Font styles to use
Sans Serif

Requirements
Must have
• Details above
Nice to have
• Would like a consistent look and feel between business card and website
Should not have
• None

```html
<!DOCTYPE html>
<html lang="en">
<head>
<meta charset="utf-8">
<title>Brolvik Architecture – Business Card</title>
<link rel="stylesheet" href="https://fonts.googleapis.com/css2?family=Oswald:wght@400;500&family=Roboto:wght@400&display=swap">
<style>
  :root {
    --backdrop: #e4e4e4;
    --card: #ffffff;
    --ink: #1c1c1c;
    --brand: #5a5a5a;
    --name: #6e6e6e;
    --rule: #bdbdbd;
    --icon-bg: #1e1e1e;
    --icon-fg: #ffffff;
  }
  * { box-sizing: border-box; margin: 0; padding: 0; }
  html, body {
    width: 1200px; height: 988px; overflow: hidden;
    background: var(--backdrop);
  }
  .stage {
    position: relative; width: 1200px; height: 988px;
  }
  .card {
    position: absolute; left: 250px; width: 700px; height: 400px;
    background: var(--card);
    box-shadow: 0 6px 18px rgba(0,0,0,.18);
  }
  .card--front { top: 74px; }
  .card--back { top: 514px; }

  .brand {
    font-family: 'Oswald', sans-serif; font-weight: 400;
    color: var(--brand); text-transform: uppercase;
    letter-spacing: .18em; white-space: nowrap;
  }
  .card--front .brand {
    position: absolute; left: 0; right: 0; top: 178px;
    text-align: center; font-size: 34px;
  }
  .card--back .brand {
    position: absolute; left: 40px; top: 112px; font-size: 22px;
  }

  .top-rule {
    position: absolute; left: 330px; right: 40px; top: 56px;
    height: 1px; background: var(--rule);
  }

  .holder {
    position: absolute; left: 40px; top: 178px; width: 330px;
    padding-bottom: 8px; border-bottom: 1px solid var(--rule);
  }
  .holder__name {
    font-family: 'Oswald', sans-serif; font-weight: 500;
    font-size: 26px; color: var(--name); text-transform: uppercase;
    letter-spacing: .02em; line-height: 1.1;
  }
  .holder__title {
    font-family: 'Roboto', sans-serif; font-size: 12px;
    color: var(--ink); text-transform: uppercase; letter-spacing: .08em;
    margin-top: 4px;
  }

  .contact-list { position: absolute; list-style: none; }
  .contact-list--left { left: 40px; top: 244px; width: 330px; }
  .contact-list--right { left: 390px; top: 88px; width: 270px; }
  .contact {
    display: flex; align-items: center; gap: 12px;
    height: 40px; border-bottom: 1px solid var(--rule);
    font-family: 'Roboto', sans-serif; font-size: 14px; color: var(--ink);
    letter-spacing: .02em; white-space: nowrap;
  }
  .contact__icon {
    flex: none; width: 24px; height: 24px; border-radius: 4px;
    background: var(--icon-bg);
    display: flex; align-items: center; justify-content: center;
  }
  .contact__icon svg { width: 14px; height: 14px; }
</style>
</head>
<body>
<main class="stage">

  <section class="card card--front" aria-label="Card front">
    <p class="brand">Brolvik Architecture</p>
  </section>

  <section class="card card--back" aria-label="Card back">
    <div class="top-rule"></div>
    <p class="brand">Brolvik Architecture</p>

    <ul class="contact-list contact-list--right">
      <li class="contact">
        <span class="contact__icon">
          <svg viewBox="0 0 16 16" fill="none" stroke="var(--icon-fg)" stroke-width="1.5"><rect x="1.5" y="3.5" width="13" height="9" rx="1"/><path d="M2 4l6 5 6-5"/></svg>
        </span>
        dale@tbrolvik.com
      </li>
      <li class="contact">
        <span class="contact__icon">
          <svg viewBox="0 0 16 16" fill="none" stroke="var(--icon-fg)" stroke-width="1.3"><circle cx="8" cy="8" r="6.5"/><ellipse cx="8" cy="8" rx="3" ry="6.5"/><path d="M1.5 8h13"/></svg>
        </span>
        www.tbrolvik.com
      </li>
    </ul>

    <div class="holder">
      <p class="holder__name">Dale Brolvik</p>
      <p class="holder__title">Principle</p>
    </div>

    <ul class="contact-list contact-list--left">
      <li class="contact">
        <span class="contact__icon">
          <svg viewBox="0 0 16 16" fill="var(--icon-fg)"><path d="M4 1.5l2.3 3-1.4 1.6c.9 2 2.5 3.6 4.5 4.5l1.6-1.4 3 2.3-1.3 2.5C7.5 13.6 2.4 8.5 1.5 3.3z"/></svg>
        </span>
        650-555-0172
      </li>
      <li class="contact">
        <span class="contact__icon">
          <svg viewBox="0 0 16 16" fill="none" stroke="var(--icon-fg)" stroke-width="1.3"><path d="M4.5 6V1.5h7V6"/><rect x="1.5" y="6" width="13" height="6" rx="1"/><path d="M4.5 10h7v4.5h-7z"/></svg>
        </span>
        650-555-0196
      </li>
      <li class="contact">
        <span class="contact__icon">
          <svg viewBox="0 0 16 16" fill="var(--icon-fg)"><path d="M8 1a5 5 0 0 0-5 5c0 3.6 5 9 5 9s5-5.4 5-9a5 5 0 0 0-5-5zm0 7a2 2 0 1 1 0-4 2 2 0 0 1 0 4z"/></svg>
        </span>
        418 Quill Lane, Menlo Park, CA 94025
      </li>
    </ul>
  </section>

</main>
</body>
</html>
```